Help me design my in store poster to promote our Loan product!

We need a design for a 2 X 3 poster inside our stores to promote our installment loan product. We are called Wade's Check Cashing, but offer loans inside our stores. We are open to a new logo for Wade's Loans, and open to any new exciting colors to stand out in the store. We provide short term monthly installment loans, we have monthly payments from 3 - 12 months. Our loans range from $100 - $1,400 with low interest. We ask for ID, consistent source of income, and credit check. We help build credit, and it is fast and easy. We want it to be simple and clean to get people's attention when they are inside our stores. Please help!

UPDATE: The design will be for a 2 X 7 poster now. Less words.

Other font styles liked:
• Rounded corners with the font

Requirements
Must have
• Bold colors, the words: loans, cash, $100 - $1,400, monthly payments, credit building, quick.
Nice to have
• A new logo, the Wade's Check Cashing logo added as reference

UPDATE: If we can add a quick slogan : FAST CASH NOW or HELP IS HERE or YOUR CASH IS HERE or LOANS FOR LIVING or LOANS FOR LIFE

A WADE'S FINANCE LOGO that looks similar to the NOVAJET logo I attached.

```html
<!DOCTYPE html>
<html lang="en">
<head>
<meta charset="utf-8">
<title>Wade's Check Cashing – Loans Poster</title>
<link rel="stylesheet" href="https://fonts.googleapis.com/css2?family=Montserrat:ital,wght@0,500;0,800;0,900;1,800&family=Oswald:wght@600;700&display=swap">
<style>
  :root {
    --brand-blue: #0a57a8;
    --accent-orange: #f7941d;
    --ink: #1f1f1f;
    --paper: #ffffff;
    --paper-shade: #f1f3f6;
    --rule: #e3e6ea;
  }
  * { margin: 0; padding: 0; box-sizing: border-box; }
  html, body { width: 812px; height: 1200px; overflow: hidden; }
  body { background: var(--paper); font-family: "Montserrat", Arial, sans-serif; color: var(--ink); }

  .poster {
    position: relative;
    width: 812px; height: 1200px;
    background: linear-gradient(180deg, var(--paper) 0%, var(--paper-shade) 60%, var(--paper) 100%);
    overflow: hidden;
  }

  .band {
    position: absolute; left: 20px; width: 772px;
    background: var(--brand-blue);
    box-shadow: 0 6px 10px rgba(0,0,0,.12);
  }
  .band svg { display: block; width: 100%; height: 100%; }
  .band--top { top: 20px; height: 99px; }
  .band--consult { top: 892px; height: 111px; }

  .display { font-family: "Oswald", "Arial Narrow", sans-serif; font-weight: 700; }
  .headline-svg { position: absolute; left: 20px; top: 128px; width: 780px; height: 64px; }
  .headline { font-family: "Montserrat", Arial, sans-serif; font-weight: 900; fill: var(--brand-blue); }

  .hero-photo {
    position: absolute; left: 511px; top: 208px; width: 301px; height: 683px;
    background:
      radial-gradient(ellipse 38% 22% at 62% 30%, #d9b8a3 0%, rgba(217,184,163,0) 100%),
      radial-gradient(ellipse 50% 14% at 60% 12%, #c9cbcd 0%, rgba(201,203,205,0) 100%),
      radial-gradient(ellipse 60% 45% at 70% 80%, #9a9da2 0%, rgba(154,157,162,0) 100%),
      linear-gradient(90deg, rgba(255,255,255,1) 0%, rgba(238,239,241,.4) 30%, #dfe1e4 100%);
    -webkit-mask-image: linear-gradient(90deg, transparent 0%, #000 25%);
            mask-image: linear-gradient(90deg, transparent 0%, #000 25%);
  }

  .burst { position: absolute; left: 20px; top: 210px; width: 125px; height: 92px; }
  .price-range { position: absolute; left: 203px; top: 218px; width: 368px; height: 84px; }

  .benefits { position: absolute; left: 20px; top: 0; width: 500px; list-style: none; }
  .benefit { position: absolute; left: 0; width: 500px; }
  .benefit__tick { position: absolute; left: 0; top: 0; width: 47px; height: 41px; }
  .benefit__title {
    position: absolute; left: 56px; top: 0;
    font-weight: 800; font-style: italic; font-size: 34px; line-height: 40px;
    color: var(--brand-blue); letter-spacing: -.4px; white-space: nowrap;
  }
  .benefit__text {
    position: absolute; left: 56px; top: 44px; width: 440px;
    font-weight: 500; font-size: 18.5px; line-height: 21px; color: var(--ink);
  }

  .divider { position: absolute; left: 453px; top: 1008px; width: 1px; height: 186px; background: var(--rule); }
  .call-svg { position: absolute; left: 36px; top: 1026px; width: 392px; height: 152px; }

  .brand-name {
    position: absolute; left: 471px; top: 1046px; width: 321px;
    text-align: center;
    font-family: "Montserrat", Arial, sans-serif; font-weight: 900;
    color: var(--brand-blue); font-size: 50px; line-height: 54px;
  }
  .brand-name span { display: block; font-size: 24px; line-height: 36px; letter-spacing: 1px; }
</style>
</head>
<body>
<main class="poster">

  <header class="band band--top">
    <svg viewBox="0 0 772 99" aria-label="We offer loans inside our stores">
      <text class="display" x="10" y="77" font-size="72" fill="#fff" textLength="752" lengthAdjust="spacingAndGlyphs">WE OFFER LOANS INSIDE OUR STORES</text>
    </svg>
  </header>

  <svg class="headline-svg" viewBox="0 0 780 64" aria-label="Want loan or cash?">
    <text class="headline" x="0" y="60" font-size="72" textLength="776" lengthAdjust="spacingAndGlyphs">WANT LOAN OR CASH?</text>
  </svg>

  <div class="hero-photo" role="img" aria-label="Photo of a smiling senior man in glasses wearing a grey sweater over a striped shirt"></div>

  <svg class="burst" viewBox="-64 -47 128 94" aria-hidden="true">
    <polygon fill="var(--accent-orange)" points="62,0 34.8,7.3 53.7,24 25.5,19.8 31,41.6 9.3,27 0,46 -9.3,27 -31,41.6 -25.5,19.8 -53.7,24 -34.8,7.3 -62,0 -34.8,-7.3 -53.7,-24 -25.5,-19.8 -31,-41.6 -9.3,-27 0,-46 9.3,-27 31,-41.6 25.5,-19.8 53.7,-24 34.8,-7.3"/>
    <text x="0" y="9" transform="rotate(-15)" text-anchor="middle" font-family="Montserrat, Arial, sans-serif" font-weight="900" font-size="26" fill="#fff">GET</text>
  </svg>

  <svg class="price-range" viewBox="0 0 368 84" aria-label="$100 - $1400">
    <text class="display" x="0" y="80" font-size="96" fill="var(--accent-orange)" textLength="362" lengthAdjust="spacingAndGlyphs"><tspan font-size="44" dy="-38">$</tspan><tspan dy="38">100 - </tspan><tspan font-size="44" dy="-38">$</tspan><tspan dy="38">1400</tspan></text>
  </svg>

  <ul class="benefits">
    <li class="benefit" style="top:346px">
      <svg class="benefit__tick" viewBox="0 0 47 41" aria-hidden="true"><circle cx="20" cy="22" r="17" fill="none" stroke="var(--accent-orange)" stroke-width="3"/><path d="M11 21 L19 30 L44 3" fill="none" stroke="var(--accent-orange)" stroke-width="3.5" stroke-linecap="round" stroke-linejoin="round"/></svg>
      <h2 class="benefit__title">SHORT TERM</h2>
      <p class="benefit__text">We provide short term monthly installment loans</p>
    </li>
    <li class="benefit" style="top:452px">
      <svg class="benefit__tick" viewBox="0 0 47 41" aria-hidden="true"><circle cx="20" cy="22" r="17" fill="none" stroke="var(--accent-orange)" stroke-width="3"/><path d="M11 21 L19 30 L44 3" fill="none" stroke="var(--accent-orange)" stroke-width="3.5" stroke-linecap="round" stroke-linejoin="round"/></svg>
      <h2 class="benefit__title">MONTHLY INSTALMENT</h2>
      <p class="benefit__text">We have monthly payments from 3 - 12 months</p>
    </li>
    <li class="benefit" style="top:558px">
      <svg class="benefit__tick" viewBox="0 0 47 41" aria-hidden="true"><circle cx="20" cy="22" r="17" fill="none" stroke="var(--accent-orange)" stroke-width="3"/><path d="M11 21 L19 30 L44 3" fill="none" stroke="var(--accent-orange)" stroke-width="3.5" stroke-linecap="round" stroke-linejoin="round"/></svg>
      <h2 class="benefit__title">LOW INTEREST RATE</h2>
      <p class="benefit__text">Our loans range from $100 - $1,400 with low interest</p>
    </li>
    <li class="benefit" style="top:665px">
      <svg class="benefit__tick" viewBox="0 0 47 41" aria-hidden="true"><circle cx="20" cy="22" r="17" fill="none" stroke="var(--accent-orange)" stroke-width="3"/><path d="M11 21 L19 30 L44 3" fill="none" stroke="var(--accent-orange)" stroke-width="3.5" stroke-linecap="round" stroke-linejoin="round"/></svg>
      <h2 class="benefit__title">QUICK &amp; EASY</h2>
      <p class="benefit__text">We ask for ID, consistent source of income, and credit check</p>
    </li>
    <li class="benefit" style="top:788px">
      <svg class="benefit__tick" viewBox="0 0 47 41" aria-hidden="true"><circle cx="20" cy="22" r="17" fill="none" stroke="var(--accent-orange)" stroke-width="3"/><path d="M11 21 L19 30 L44 3" fill="none" stroke="var(--accent-orange)" stroke-width="3.5" stroke-linecap="round" stroke-linejoin="round"/></svg>
      <h2 class="benefit__title">BUILD CREDIT</h2>
      <p class="benefit__text">We help build credit, and it is fast and easy</p>
    </li>
  </ul>

  <section class="band band--consult">
    <svg viewBox="0 0 772 111" aria-label="For free consultation">
      <text class="display" x="16" y="92" font-size="98" fill="#fff" textLength="740" lengthAdjust="spacingAndGlyphs">FOR FREE CONSULTATION</text>
    </svg>
  </section>

  <svg class="call-svg" viewBox="0 0 392 152" aria-label="Call us now! 555-014-2600">
    <text class="display" x="0" y="70" font-size="88" fill="var(--brand-blue)" textLength="390" lengthAdjust="spacingAndGlyphs">CALL US NOW!</text>
    <text class="display" x="0" y="148" font-size="96" fill="var(--accent-orange)" textLength="388" lengthAdjust="spacingAndGlyphs">555-014-2600</text>
  </svg>

  <div class="divider"></div>

  <p class="brand-name">WADE'S<span>CHECK CASHING</span></p>

</main>
</body>
</html>
```